Print materials for 3-star hotel

We are changing up our print materials (notepads, letterheads, key card jackets, small flyer for the room rates) We are a 3 star business hotel in the Philippines and have mainly used grey tones and clean, simple lines. See attached photos for logo and hotel interior photos.

Target Market(s)

Business

Contact Information for Business Card

Tamarind Crest Hotel
Governor Lualhati Avenue corner Pindang St Cebu City 6000 Philippines
Tel: +63 32 480 5273
Mobile: +63 917 608 4926
www.tamarindcresthotel.example

Font styles to use
Serif
Sans Serif

Requirements
Must have
• Simple
• Readable font and font size
Nice to have
• Neutral colors, grey and taupes
Should not have
• No purples and bright blues

```html
<!DOCTYPE html>
<html lang="en">
<head>
<meta charset="utf-8">
<title>Tamarind Crest Hotel – Business Card</title>
<link href="https://fonts.googleapis.com/css2?family=Cinzel:wght@400&family=Roboto:wght@400;500&display=swap" rel="stylesheet">
<style>
  :root {
    --backdrop: #2b2b2b;
    --card: #1c1c1c;
    --ink: #f2f2f2;
    --ink-soft: #e6e6e6;
    --serif: "Cinzel", "Times New Roman", serif;
    --sans: "Roboto", Arial, sans-serif;
  }
  * { margin: 0; padding: 0; box-sizing: border-box; }
  html, body { width: 1200px; height: 960px; overflow: hidden; }
  body { background: var(--backdrop); position: relative; font-family: var(--sans); color: var(--ink); }

  .card { position: absolute; background: var(--card); box-shadow: 0 4px 10px rgba(0,0,0,.45); }
  .card--front { left: 316px; top: 113px; width: 598px; height: 344px; }
  .card--back  { left: 313px; top: 474px; width: 598px; height: 340px; }

  /* Front */
  .brand { position: absolute; left: 52px; top: 44px; width: 232px; text-align: center; font-family: var(--serif); color: var(--ink); }
  .brand__square { display: block; width: 34px; height: 34px; margin: 6px auto 22px; background: var(--ink); }
  .brand__name { display: block; font-size: 19px; letter-spacing: 3px; line-height: 1; }
  .brand__sub { display: block; font-size: 19px; letter-spacing: 3px; line-height: 1; margin-top: 8px; }

  .holder { position: absolute; left: 52px; top: 212px; }
  .holder__name { font-family: var(--serif); font-size: 23px; line-height: 1; letter-spacing: .5px; }
  .holder__title { font-family: var(--sans); font-weight: 500; font-size: 15px; margin-top: 5px; letter-spacing: .2px; }

  .contact { position: absolute; left: 372px; top: 165px; font-size: 14.5px; color: var(--ink-soft); list-style: none; }
  .contact__address { line-height: 18px; margin-bottom: 10px; }
  .contact__row { display: flex; align-items: center; height: 19px; }
  .contact__row svg { width: 14px; height: 14px; margin-right: 9px; fill: var(--ink); flex: none; }

  /* Back */
  .back-brand { position: absolute; left: 0; right: 0; top: 106px; text-align: center; font-family: var(--serif); }
  .back-brand__square { display: block; width: 44px; height: 44px; margin: 0 auto 26px; background: var(--ink); }
  .back-brand__name { font-size: 26px; letter-spacing: 4px; line-height: 1; }
  .back-web { position: absolute; left: 0; right: 0; top: 284px; text-align: center; font-size: 15px; letter-spacing: 5.5px; color: var(--ink-soft); }
</style>
</head>
<body>

<section class="card card--front">
  <div class="brand">
    <span class="brand__square"></span>
    <span class="brand__name">TAMARIND CREST</span>
    <span class="brand__sub">HOTEL</span>
  </div>

  <div class="holder">
    <p class="holder__name">MARCO VILLANUEVA</p>
    <p class="holder__title">CEO/FOUNDER</p>
  </div>

  <ul class="contact">
    <li class="contact__address">2140 Sampaguita Lane<br>Cebu City, Cebu 6000</li>
    <li class="contact__row">
      <svg viewBox="0 0 16 16" aria-hidden="true"><path d="M3.6 1.2l2.2 2.6-1.3 1.9c.9 2 2.4 3.6 4.4 4.5l1.9-1.3 2.6 2.2-1 2.6C7 13.6 2.4 9 1 3.2z"/></svg>
      032 480 5273
    </li>
    <li class="contact__row">
      <svg viewBox="0 0 16 16" aria-hidden="true"><path d="M4.5 0.5h7v15h-7zM6 2v10h4V2zM7.3 13h1.4v1.2H7.3z" fill-rule="evenodd"/></svg>
      0917 608 4926
    </li>
    <li class="contact__row">
      <svg viewBox="0 0 16 16" aria-hidden="true"><path d="M4 1h8v4H4zM1 6h14v6h-3v3H4v-3H1zM5 10v4h6v-4z" fill-rule="evenodd"/></svg>
      032 480 5274
    </li>
    <li class="contact__row">
      <svg viewBox="0 0 16 16" aria-hidden="true"><path d="M1 3.5h14v1L8 9 1 4.5zM1 6l7 4.5L15 6v6.5H1z"/></svg>
      stay@tamarindcrest.example
    </li>
    <li class="contact__row">
      <svg viewBox="0 0 16 16" aria-hidden="true"><path d="M8 1a7 7 0 1 0 0 14A7 7 0 0 0 8 1zm-1 2.2c-.6 1-.4 2 .5 2.4.8.4.6 1.6-.3 1.6-1 0-1.7.8-1.3 1.8.4.9 1.4 1 1.6 2 .1.8-.2 1.6-.7 2A5.6 5.6 0 0 1 7 3.2zm3 .4a5.6 5.6 0 0 1 3.3 6.6c-.6-.6-1.6-.5-2-1.3-.4-.9.6-1.6 0-2.4-.5-.6-1.7-.2-1.8-1.1 0-.6.4-1.1.5-1.8z"/></svg>
      www.tamarindcrest.example
    </li>
  </ul>
</section>

<section class="card card--back">
  <div class="back-brand">
    <span class="back-brand__square"></span>
    <p class="back-brand__name">TAMARIND CREST HOTEL</p>
  </div>
  <p class="back-web">www.tamarindcrest.example</p>
</section>

</body>
</html>
```